Brellick Commercial Roof Restoration LLC needs billboard and banner designs

Need billboard ad design for small commercial roof restoration company. Looking for a billboard design that can be used on digital and hard print billboards. Also need banner design for 4' x 8' job site banners that will go by roadside to draw potential customers to our brand. Our vision for bill board would show an attractive women in business dress, clearly in a building having to use an (red) umbrella (inside building) due to leaking roof. Caption "WE CAN HELP" www.BRELLICKCOMMERCIALROOF.example
For banner design we would use some before/after roof photos (attached, blend/overlay at an angle) in background with "Another Quality Commercial Roof Restoration By:" "Brellick Commercial Roof LLC" "Is your commercial roof leaking? Call 555.318.4726 for help".
All final designs should communicate commercial roof restoration only.
Target Market(s)
Commercial building owner/managers
Industry/Entity Type
Roofing
Font styles to use
Requirements
Must have
- Just added a Jpeg file of a logo of the company that we buy our products from. This logo & "Certified Premier Installers" needs to be added to the project. It only needs to have a small footprint on the ad. Contact me if you have questions. Thank you.
Nice to have
- Billboard design; our name, website, relay our message with image. As described above in project description
Banner; Our name, phone number and bold written message

```html
<!DOCTYPE html>
<html lang="en">
<head>
<meta charset="utf-8">
<title>Brellick Commercial Roof LLC – Job Site Banner</title>
<link rel="stylesheet" href="https://fonts.googleapis.com/css2?family=Bebas+Neue&family=Open+Sans:wght@600;700&display=swap">
<style>
  :root {
    --page: #ffffff;
    --red: #d9473c;
    --red-deep: #b5302d;
    --blue: #1f63ab;
    --blue-deep: #1b3a63;
    --brand-red: #c6281f;
    --navy: #1f4a8c;
    --white: #ffffff;
    --plate: rgba(236, 240, 245, 0.82);
  }
  * { margin: 0; padding: 0; box-sizing: border-box; }
  html, body {
    width: 1200px;
    height: 1200px;
    overflow: hidden;
    background: var(--page);
  }
  .banner {
    position: absolute;
    left: 50px;
    top: 325px;
    width: 1100px;
    height: 549px;
    background: var(--white);
    box-shadow: 0 4px 14px rgba(0, 0, 0, 0.25);
    overflow: hidden;
  }
  .banner__photo {
    position: absolute;
    left: 0;
    top: 0;
    width: 1100px;
    height: 434px;
  }
  .headline {
    position: absolute;
    left: 0;
    top: 80px;
    width: 1100px;
    text-align: center;
    font-family: "Bebas Neue", "Arial Narrow", sans-serif;
    font-size: 95px;
    line-height: 82px;
    color: var(--white);
    letter-spacing: 0.5px;
  }
  .company-plate {
    position: absolute;
    left: 98px;
    top: 260px;
    width: 904px;
    height: 97px;
    background: var(--plate);
    display: flex;
    align-items: center;
    justify-content: center;
  }
  .company-plate__name {
    font-family: "Bebas Neue", "Arial Narrow", sans-serif;
    font-size: 80px;
    line-height: 1;
    color: var(--brand-red);
    padding-top: 8px;
  }
  .footer-strip {
    position: absolute;
    left: 0;
    top: 434px;
    width: 1100px;
    height: 115px;
    display: flex;
    align-items: center;
    font-family: "Open Sans", Arial, sans-serif;
  }
  .brand-mark {
    margin-left: 46px;
    display: flex;
    align-items: center;
    gap: 8px;
    font-weight: 700;
    font-size: 22px;
    color: var(--navy);
    letter-spacing: 0.5px;
  }
  .brand-mark__square {
    width: 18px;
    height: 18px;
    background: var(--brand-red);
  }
  .question {
    margin-left: 28px;
    font-weight: 600;
    font-size: 31px;
    line-height: 27px;
    color: var(--brand-red);
    letter-spacing: -0.5px;
  }
  .divider {
    margin-left: 18px;
    width: 20px;
    height: 64px;
  }
  .call {
    margin-left: 18px;
    font-weight: 600;
    font-size: 32px;
    color: var(--navy);
    white-space: nowrap;
  }
  .call__number {
    font-weight: 700;
    font-size: 50px;
    letter-spacing: -0.5px;
  }
</style>
</head>
<body>
  <section class="banner">
    <svg class="banner__photo" viewBox="0 0 1100 434" role="img" aria-label="Before and after photos of a commercial metal roof, blended at an angle: worn roof tinted red on the left, restored roof tinted blue on the right">
      <defs>
        <linearGradient id="before-tint" x1="0" y1="0" x2="0" y2="1">
          <stop offset="0" stop-color="#c2403c"/>
          <stop offset="0.5" stop-color="#d74a3e"/>
          <stop offset="1" stop-color="#e25a48"/>
        </linearGradient>
        <linearGradient id="after-tint" x1="0" y1="0" x2="0" y2="1">
          <stop offset="0" stop-color="#1b3a63"/>
          <stop offset="0.45" stop-color="#1e4f86"/>
          <stop offset="1" stop-color="#2268b0"/>
        </linearGradient>
      </defs>
      <rect x="0" y="0" width="1100" height="434" fill="url(#after-tint)"/>
      <polygon points="0,0 622,0 547,434 0,434" fill="url(#before-tint)"/>
    </svg>

    <h1 class="headline">Another Quality Commercial<br>Roof Restoration By</h1>

    <div class="company-plate">
      <span class="company-plate__name">Brellick Commercial Roof LLC</span>
    </div>

    <div class="footer-strip">
      <div class="brand-mark">
        <span class="brand-mark__square"></span>
        <span class="brand-mark__name">BRELLICK</span>
      </div>
      <p class="question">Is your commercial<br>roof leaking?</p>
      <svg class="divider" viewBox="0 0 20 64" aria-hidden="true">
        <line x1="12" y1="2" x2="2" y2="62" stroke="#c6281f" stroke-width="2"/>
        <line x1="18" y1="2" x2="8" y2="62" stroke="#1f4a8c" stroke-width="2"/>
      </svg>
      <p class="call">Call <span class="call__number">555.318.4726</span> for help</p>
    </div>
  </section>
</body>
</html>
```